Bamboo Roofs - Where Everyday Hands can Reshape Futures

I am producing a book about humanitarian work done by Australians in Cambodia, mainly house building in poor villages. The images uploaded have been selected to link to the word 'Roofs' which emphasize Australians and Cambodians working together to bring about meaningful change in the lives of the recipients as well as those giving. The book is a coffee table type book with 50% text 50% images, telling of work done over the last 15 years. Cambodians save a little for their house but the majority is donated by Australians who travel there and actually help build the houses. The lives of both are changed in the process. The book will be landscape format. I have two more images which I am unable to upload - I can attach to an email. I have some text to give you for the back cover, a logo for back cover page, which is attached and authors names: Ray Tindall and Doug Abernethy.
The back cover text is here:
'Approaching retirement, Ross and Delia Fenwick decided to use their organisational skills and knowledge in Cambodia to help those less fortunate than themselves own a simple house. They also wanted to empower other West Australians to join them in this work.
Ross and Delia subsequently created a hands-on volunteering experience where people didn’t just give or raise money to help to build these houses but went to Cambodia to complete their construction.
This book tells the powerful stories of some volunteers, including Harbourside Falcons football players and their mothers, who became involved in this work, the people they helped and how lives were transformed.
Target Market(s)
Australians of any age who might be interested in becoming involved - who want serious (meaningful) fun (doing different things in exotic locations)
Industry/Entity Type
Humanitarian work
Colors
Designer to choose colors to be used in the design.
Requirements
Must have
- The image 'tobybrant' is of a couple of famous sports people and we would like it to be easily viewed though not dominant
Nice to have
- Young and old volunteers - there is no stereotype
Should not have
- Any negative portrayals of Cambodians - not poor, but joyous. It should not suggest giving but experiencing.

```html
<!DOCTYPE html>
<html lang="en">
<head>
<meta charset="utf-8">
<title>Bamboo Roofs – Book Cover</title>
<link rel="stylesheet" href="https://fonts.googleapis.com/css2?family=League+Gothic&family=Arimo:wght@700&display=swap">
<style>
  :root {
    --navy: #262e5f;
    --red: #c41f30;
    --white: #ffffff;
    --page: #f2f2f0;
    --gap: 7px;
  }
  html, body {
    margin: 0;
    padding: 0;
    width: 1200px;
    height: 1200px;
    overflow: hidden;
    background: var(--page);
  }
  .canvas {
    position: relative;
    width: 1200px;
    height: 1200px;
  }
  .cover {
    position: absolute;
    left: 60px;
    top: 185px;
    width: 1080px;
    height: 830px;
    background: var(--white);
    border: 4px solid var(--navy);
    box-sizing: border-box;
    overflow: hidden;
  }
  .photo-row {
    position: absolute;
    left: 0;
    width: 100%;
    display: grid;
    grid-template-columns: 1fr 1fr 1fr;
    gap: var(--gap);
  }
  .photo-row--top { top: 0; height: 212px; }
  .photo-row--bottom { bottom: 0; height: 206px; }
  .photo { width: 100%; height: 100%; }
  .photo--crowd-kids { background: linear-gradient(160deg, #8b7a66, #b59b82 55%, #6d6a70); }
  .photo--volunteers-purple { background: linear-gradient(170deg, #a8b7a0, #7a55a8 55%, #5f6b4a); }
  .photo--house-frame { background: linear-gradient(180deg, #a9c6e8 0%, #cfe0ef 40%, #4f6f5a 60%, #86a86a); }
  .photo--two-volunteers { background: linear-gradient(160deg, #5c7a48, #e6e2dc 55%, #3b3f4a); }
  .photo--players-kids { background: linear-gradient(180deg, #4f7a68, #8c8a80 50%, #2c2c30); }
  .photo--village-celebration { background: linear-gradient(180deg, #6d9a74, #c58a7e 55%, #5c6fa0); }

  .title-band {
    position: absolute;
    left: 0;
    top: 218px;
    width: 100%;
    height: 400px;
    background: var(--red);
  }
  .label-bar {
    position: absolute;
    background: var(--navy);
    color: var(--white);
    font-family: "Arimo", Arial, sans-serif;
    font-weight: 700;
    text-transform: uppercase;
    display: flex;
    align-items: center;
    justify-content: center;
    letter-spacing: 0.5px;
  }
  .label-bar--authors {
    top: 0;
    left: 160px;
    width: 790px;
    height: 54px;
    font-size: 29px;
  }
  .label-bar--subtitle {
    bottom: 0;
    left: 150px;
    width: 790px;
    height: 52px;
    font-size: 28px;
  }
  .book-title {
    position: absolute;
    left: 0;
    right: 0;
    top: 68px;
    margin: 0;
    text-align: center;
    font-family: "League Gothic", "Arial Narrow", sans-serif;
    font-weight: 400;
    font-size: 218px;
    line-height: 1;
    color: var(--white);
    text-transform: uppercase;
    letter-spacing: 2px;
    transform: scaleY(1.3);
    transform-origin: top center;
  }
</style>
</head>
<body>
<div class="canvas">
  <section class="cover">
    <div class="photo-row photo-row--top">
      <div class="photo photo--crowd-kids" role="img" aria-label="Smiling volunteer crouching among a crowd of laughing village children"></div>
      <div class="photo photo--volunteers-purple" role="img" aria-label="Four volunteers in matching purple t-shirts holding tools at a build site"></div>
      <div class="photo photo--house-frame" role="img" aria-label="Volunteers and villagers building a raised house on stilts under a blue sky"></div>
    </div>

    <div class="title-band">
      <div class="label-bar label-bar--authors">Ray Tindall and Doug Abernethy</div>
      <h1 class="book-title">Bamboo Roofs</h1>
      <div class="label-bar label-bar--subtitle">Where Everyday Hands Can Reshape Futures</div>
    </div>

    <div class="photo-row photo-row--bottom">
      <div class="photo photo--two-volunteers" role="img" aria-label="Two smiling volunteers wearing traditional checked scarves on a village road"></div>
      <div class="photo photo--players-kids" role="img" aria-label="Two football players standing with village children beside a new house ladder"></div>
      <div class="photo photo--village-celebration" role="img" aria-label="Villagers and volunteers cheering with raised arms in front of a finished house"></div>
    </div>
  </section>
</div>
</body>
</html>
```